Flyer für Anbieter einer Fortbildung für Beratungslehrer
Zielgruppe
Wir bieten eine Fortbildung für Beratungslehrer an, welche mit immer komplexer werdenden psychischen Fällen arbeiten. Diese Fortbildung setzt sich gezielt mit der Stärkung des Selbstkonzepts, der Resilienz sowie dem Selbstwert auseinander. Wir stellen dabei die Anliegen der Klienten in den Fokus.
Das Angebot basiert auf dem Konzept des Lernfeld Zuversicht des Kurt- Wendland-Institut, Heidelberg
Aufgabenstellung
Die Inhalte der Fortbildung sollen enthalten sein.
Layout sollte unseren Arbeitsbereich im psychologischen Wohlbefinden widerspiegeln

```html
<!DOCTYPE html>
<html lang="de">
<head>
<meta charset="utf-8">
<title>Fortbildung für Beratungslehrer – Flyer</title>
<link href="https://fonts.googleapis.com/css2?family=Inter:wght@300;400;600&display=swap" rel="stylesheet">
<style>
  :root {
    --backdrop: #364857;
    --paper: #ffffff;
    --green: #5a9a6a;
    --green-light: #80b584;
    --green-dark: #3f5f46;
    --sage-grey: #a8b0ab;
    --teal-soft: #a9d4cc;
    --ink: #3a342a;
    --white: #ffffff;
  }
  * { margin: 0; padding: 0; box-sizing: border-box; }
  html, body { width: 1200px; height: 1200px; overflow: hidden; }
  body {
    background: var(--backdrop);
    font-family: "Inter", "Helvetica Neue", Arial, sans-serif;
    font-weight: 300;
    color: var(--ink);
    position: relative;
  }
  .page { position: absolute; background: var(--paper); overflow: hidden; }
  .page--front { left: 49px; top: 213px; width: 575px; height: 816px; }
  .page--back { left: 658px; top: 170px; width: 492px; height: 700px; }
  .abs { position: absolute; }

  /* Front */
  .header-photo {
    left: 285px; top: 24px; width: 262px; height: 74px;
    background: linear-gradient(135deg, #4c6e50, #2f4a36);
  }
  .eyebrow-band {
    left: 0; top: 44px; width: 405px; height: 42px;
    background: var(--green-light); color: var(--white);
    font-size: 19px; letter-spacing: 0.3px;
    display: flex; align-items: center; padding-left: 88px;
  }
  .title-band {
    left: 0; top: 98px; width: 575px; height: 124px;
    background: var(--green); color: var(--white);
    padding: 24px 0 0 27px;
  }
  .title-band h1 {
    font-weight: 300; font-size: 32.5px; line-height: 38px; letter-spacing: 0.4px;
  }
  .intro-box {
    left: 15px; top: 254px; width: 256px; height: 237px;
    border: 2.5px solid var(--ink);
    display: flex; align-items: center; justify-content: center;
    text-align: center; font-size: 17.5px; line-height: 23px; font-weight: 400;
    padding: 0 14px;
  }
  .hero-photo {
    left: 285px; top: 222px; width: 262px; height: 267px;
    background: linear-gradient(160deg, #55795d 0%, #6d8c72 45%, #b8c8d6 80%, #e6e6e2 100%);
  }
  .expect-section {
    left: 0; top: 509px; width: 575px; height: 307px;
    background: var(--sage-grey); color: var(--white);
  }
  .expect-section h2 {
    position: absolute; left: 0; width: 575px; top: 21px;
    text-align: center; font-weight: 300; font-size: 23.5px; letter-spacing: 0.5px;
  }
  .expect-item {
    position: absolute; top: 81px; font-size: 15.5px; line-height: 19.8px; width: 140px;
  }
  .expect-item--1 { left: 32px; width: 145px; }
  .expect-item--2 { left: 225px; }
  .expect-item--3 { left: 404px; width: 145px; }
  .divider { position: absolute; top: 84px; width: 1.5px; height: 194px; background: var(--ink); }
  .divider--1 { left: 197px; }
  .divider--2 { left: 377px; }

  /* Back */
  .lead-box {
    left: 26px; top: 19px; width: 441px; height: 109px;
    border: 2.5px solid var(--ink);
    padding: 9px 16px 0 18px;
    font-size: 13px; line-height: 17px; font-weight: 400;
  }
  .concept-photo {
    left: 190px; top: 140px; width: 302px; height: 158px;
    background: linear-gradient(120deg, #a3d2c9, #c6e3dd 60%, #e8d6c7 100%);
  }
  .concept-box {
    left: 0; top: 159px; width: 327px; height: 181px;
    background: var(--sage-grey); color: var(--white);
    padding: 12px 16px 0 29px;
  }
  .concept-box h3 { font-size: 15px; line-height: 20px; font-weight: 600; letter-spacing: 0.6px; margin-bottom: 6px; }
  .concept-box p { font-size: 13px; line-height: 17px; }
  .audience {
    left: 20px; top: 345px; width: 447px; text-align: right;
  }
  .audience h3 { font-size: 15px; line-height: 20px; font-weight: 600; letter-spacing: 0.6px; margin-bottom: 6px; }
  .audience p { font-size: 13px; line-height: 17px; font-weight: 400; }
  .booking-band {
    left: 0; top: 390px; width: 492px; height: 150px;
    background: var(--green-light); color: var(--white);
    text-align: center; padding-top: 12px;
  }
  .booking-band h2 { font-weight: 300; font-size: 20.5px; letter-spacing: 0.5px; }
  .closing {
    left: 0; top: 639px; width: 492px; text-align: center;
    color: var(--green); font-weight: 600; font-size: 15.5px; line-height: 20px; letter-spacing: 0.5px;
  }
</style>
</head>
<body>
  <section class="page page--front">
    <div class="abs header-photo" role="img" aria-label="Fotoausschnitt in dunklem Grün"></div>
    <div class="abs eyebrow-band">Fortbildung für Beratungslehrer:</div>
    <div class="abs title-band">
      <h1>Stärkung des Selbstkonzepts,<br>des Selbstwerts und der Resilienz</h1>
    </div>
    <div class="abs intro-box">
      <p>Sie sind Beratungslehrer und möchten Ihre Klient*innen bestmöglich in ihrer persönlichen Entwicklung unterstützen? Dann ist diese Fortbildung genau das Richtige für Sie!</p>
    </div>
    <div class="abs hero-photo" role="img" aria-label="Foto einer nachdenklichen jungen Frau am Laptop vor grüner Wand"></div>
    <div class="abs expect-section">
      <h2>Was erwartet Sie?</h2>
      <p class="expect-item expect-item--1">Stärkung des Selbstkonzepts: Erfahren Sie, wie Sie Klient*innen helfen können, ein gesundes und positives Selbstbild zu entwickeln.</p>
      <span class="divider divider--1"></span>
      <p class="expect-item expect-item--2">Aufbau von Selbstwert: Entdecken Sie Wege, um das Selbstvertrauen und die Eigenmotivation Ihrer Klient*innen nachhaltig zu fördern.</p>
      <span class="divider divider--2"></span>
      <p class="expect-item expect-item--3">Förderung der Resilienz: Lernen Sie Strategien kennen, mit denen Klient*innen Krisen und Herausforderungen besser bewältigen können.</p>
    </div>
  </section>

  <section class="page page--back">
    <div class="abs lead-box">
      <p>In dieser praxisorientierten Fortbildung lernen Sie, wie Sie Ihre Klient*innen gezielt in den Bereichen Selbstkonzept, Selbstwert und Resilienz stärken können. Basierend auf dem bewährten Konzept des Lernfeld Zuversicht werden Ihnen Methoden und Techniken vermittelt, die direkt in der Beratung anwendbar sind.</p>
    </div>
    <div class="abs concept-photo" role="img" aria-label="Foto von Händen, die eine farbige Kopf-Silhouette mit Gehirn halten"></div>
    <div class="abs concept-box">
      <h3>Warum das Lernfeld<br>Zuversicht?</h3>
      <p>Das Lernfeld Zuversicht verbindet positive Psychologie mit pädagogischen Ansätzen und ermöglicht eine ganzheitliche Förderung der Persönlichkeit. Ziel ist es, Klient*innen auf ein erfülltes und zufriedenes Leben vorzubereiten.</p>
    </div>
    <div class="abs audience">
      <h3>Für wen ist die<br>Fortbildung geeignet?</h3>
      <p>Diese Fortbildung richtet sich an Beratungslehrer, Schulpsychologen und pädagogische Fachkräfte, die ihre Kompetenzen erweitern und ihre Klient*innen bestmöglich unterstützen möchten.</p>
    </div>
    <div class="abs booking-band">
      <h2>Termine und Anmeldung</h2>
    </div>
    <p class="abs closing">Investieren Sie in die Zukunft Ihrer Klient*innen – und<br>in Ihre eigene Weiterbildung!</p>
  </section>
</body>
</html>
```